A6 Flyers for sports betting / sports advisory service

WE are looking for flyer design for our business to promote a new promo. The flyer must be in similar colours to our website www.gavelcrestodds.com.au.

the flyer must contain a small intro to who we are and what we do as well as details of how to subscribe to our website etc. It must be eye catching as these will be given out to potential customers as sporting events etc

Target Market(s)

Sports Bettors / Gamblers

Industry/Entity Type

Gambling

Font styles to use
Serif

Requirements
Must have
• Catchy look and layout in colours similar to our website
Nice to have
• scan code
Should not have
• None

```html
<!DOCTYPE html>
<html lang="en">
<head>
<meta charset="utf-8">
<title>Gavelcrest Odds – Flyer</title>
<link rel="stylesheet" href="https://fonts.googleapis.com/css2?family=Inter:wght@300&display=swap">
<style>
  :root {
    --paper: #ffffff;
    --ink: #000000;
    --turf: #78a83d;
    --turf-light: #82b24a;
    --turf-dark: #6a9935;
    --turf-text: #6e9e38;
  }
  * { margin: 0; padding: 0; box-sizing: border-box; }
  html, body {
    width: 849px;
    height: 1200px;
    overflow: hidden;
    background: var(--paper);
  }
  .flyer {
    position: relative;
    width: 849px;
    height: 1200px;
    font-family: "Inter", "Helvetica Neue", Arial, sans-serif;
    font-weight: 300;
    color: var(--turf-text);
  }
  .backdrop {
    position: absolute;
    left: 0;
    top: 0;
    width: 849px;
    height: 1200px;
  }
  .headline {
    position: absolute;
    left: 137.5px;
    top: 138.5px;
    width: 513px;
    height: 544px;
  }
  .intro {
    position: absolute;
    left: 196px;
    top: 781px;
    width: 400px;
    text-align: center;
    font-size: 13.4px;
    line-height: 17px;
  }
  .site-link {
    position: absolute;
    left: 0;
    top: 914px;
    width: 793px;
    text-align: center;
    font-size: 21px;
    letter-spacing: 0.2px;
  }
  .contact-row {
    position: absolute;
    left: 0;
    top: 997px;
    width: 793px;
    height: 36px;
  }
  .social-dot {
    position: absolute;
    top: 0;
    width: 35px;
    height: 35px;
    border-radius: 50%;
    background: var(--turf);
  }
  .social-dot.left { left: 216px; }
  .social-dot.right { left: 542px; }
  .brand-name {
    position: absolute;
    left: 0;
    width: 793px;
    top: 5px;
    text-align: center;
    font-size: 21px;
    line-height: 26px;
    color: var(--turf-text);
  }
  .legal {
    position: absolute;
    left: 0;
    top: 1097px;
    width: 793px;
    text-align: center;
    font-size: 11.2px;
    letter-spacing: 1.9px;
  }
</style>
</head>
<body>
  <main class="flyer">
    <svg class="backdrop" viewBox="0 0 849 1200" aria-hidden="true">
      <defs>
        <linearGradient id="turf-panel" x1="0" y1="0" x2="0.3" y2="1">
          <stop offset="0" stop-color="#7cad44"/>
          <stop offset="0.5" stop-color="#72a23c"/>
          <stop offset="1" stop-color="#7aab42"/>
        </linearGradient>
      </defs>
      <rect class="sheet" x="0" y="44" width="793" height="1156" fill="var(--ink)"/>
      <polygon class="side-panel" points="793,44 849,0 849,1200 793,1200" fill="url(#turf-panel)"/>
    </svg>

    <svg class="headline" viewBox="263 265 981 1041" role="img" aria-label="WIN! WIN! WIN!">
      <defs>
        <linearGradient id="turf-letters" x1="0" y1="0" x2="1" y2="1">
          <stop offset="0" stop-color="var(--turf-light)"/>
          <stop offset="0.45" stop-color="var(--turf)"/>
          <stop offset="1" stop-color="var(--turf-dark)"/>
        </linearGradient>
        <g id="win-word">
          <polygon points="263,273 350,273 405,420 463,273 508,273 563,420 617,273 703,273 595,572 528,572 485,445 437,572 372,572"/>
          <rect x="721" y="273" width="81" height="299"/>
          <polygon points="849,273 929,273 1032,432 1032,273 1112,273 1112,572 1032,572 930,414 930,572 849,572"/>
          <polygon points="1172,265 1243,265 1240,495 1175,495"/>
          <circle cx="1207" cy="543" r="37"/>
        </g>
      </defs>
      <g fill="url(#turf-letters)">
        <use href="#win-word"/>
        <use href="#win-word" transform="translate(0 363)"/>
        <use href="#win-word" transform="translate(0 726)"/>
      </g>
    </svg>

    <p class="intro">When you want daily sports tips and strategies that you can rely on, Gavelcrest Odds is the way to go – every time. Our team of experienced sports betting analysts have access to a range of sports across the globe, and cater to punting fanatics anywhere in the world!</p>

    <p class="site-link">http://gavelcrestodds.com.au/</p>

    <div class="contact-row">
      <span class="social-dot left" aria-hidden="true"></span>
      <p class="brand-name">Gavelcrest Odds</p>
      <span class="social-dot right" aria-hidden="true"></span>
    </div>

    <p class="legal">© Copyright 2015 | All Rights Reserved</p>
  </main>
</body>
</html>
```